Beacon Guard Services

Our Company is a security business which needs a cut edge design, the final product should have all relevant information and maintain a bold but modern and professional look.

Target Market(s)

A cut edge design which will attract any audience

Industry/Entity Type

Security

Contact Information for Business Card

BEACON GUARD SERVICES

Daniel Hofstra
Operations Manager
Phone: 0412 739 215

Email: info@beaconguard.com.au
Web: www.beaconguard.com.au

Requirements
Must have
• Must be double sided and contain all relevant information and the company logo.

```html
<!DOCTYPE html>
<html lang="en">
<head>
<meta charset="utf-8">
<title>Beacon Guard Services – Business Card</title>
<link rel="stylesheet" href="https://fonts.googleapis.com/css2?family=Open+Sans:wght@400;600;700&display=swap">
<style>
  :root {
    --stage: #e6e7e8;
    --teal: #557379;
    --teal-dark: #3d575c;
    --teal-light: #7a9599;
    --orange: #f0a02a;
    --orange-deep: #e88a14;
    --ink: #1f2a30;
    --white: #ffffff;
  }
  * { box-sizing: border-box; margin: 0; padding: 0; }
  html, body {
    width: 1200px; height: 951px; overflow: hidden;
    background: var(--stage);
    font-family: "Open Sans", Arial, sans-serif;
  }
  .canvas { position: relative; width: 1200px; height: 951px; }

  .card {
    position: absolute;
    width: 560px; height: 320px;
    border-radius: 22px;
    overflow: hidden;
    box-shadow: 0 6px 18px rgba(0,0,0,0.25);
  }

  /* Back side */
  .card--back {
    left: 70px; top: 110px;
    background: radial-gradient(ellipse at 45% 30%, var(--teal-light) 0%, var(--teal) 45%, var(--teal-dark) 100%);
    color: var(--white);
  }
  .back-brand {
    position: absolute; left: 0; right: 0; top: 96px;
    display: flex; flex-direction: column; align-items: center; gap: 16px;
  }
  .brand-mark {
    width: 58px; height: 58px; border-radius: 50%;
    background: var(--orange);
    flex: none;
  }
  .back-brand .brand-name {
    font-weight: 700; font-size: 34px; letter-spacing: 1px;
    color: var(--white);
  }
  .back-web {
    position: absolute; left: 0; right: 0; bottom: 44px;
    text-align: center; font-size: 18px; letter-spacing: 2px;
    font-weight: 600;
  }

  /* Front side */
  .card--front {
    left: 570px; top: 450px;
    background: var(--white);
  }
  .front-brand {
    position: absolute; left: 38px; top: 40px;
    display: flex; align-items: center; gap: 12px;
  }
  .front-brand .brand-mark { width: 40px; height: 40px; }
  .front-brand .brand-name {
    font-weight: 700; font-size: 20px; color: var(--teal-dark);
    line-height: 1.1;
  }
  .person {
    position: absolute; right: 34px; top: 48px; text-align: left;
  }
  .person-name { font-size: 21px; font-weight: 600; color: var(--ink); }
  .person-role { font-size: 15px; color: var(--orange-deep); margin-top: -2px; }

  .wave { position: absolute; left: 0; top: 0; width: 560px; height: 320px; }

  .address, .contacts {
    position: absolute; color: var(--white);
    font-size: 15px; font-weight: 600; line-height: 21px;
    white-space: nowrap;
  }
  .address { left: 48px; top: 216px; }
  .contacts { left: 300px; top: 204px; }
  .line { display: flex; align-items: center; gap: 8px; }
  .line svg { width: 13px; height: 13px; flex: none; }
  .address .indent { padding-left: 21px; }
</style>
</head>
<body>
<main class="canvas">

  <section class="card card--back" aria-label="Card back">
    <div class="back-brand">
      <span class="brand-mark"></span>
      <span class="brand-name">Beacon Guard Services</span>
    </div>
    <p class="back-web">www.beaconguard.com.au</p>
  </section>

  <section class="card card--front" aria-label="Card front">
    <svg class="wave" viewBox="0 0 560 320" preserveAspectRatio="none" aria-hidden="true">
      <path d="M0 150 C120 110 230 110 330 140 C420 166 500 150 560 120 L560 320 L0 320 Z" fill="var(--orange)"/>
      <path d="M0 172 C120 128 230 128 330 158 C420 184 500 172 560 142 L560 320 L0 320 Z" fill="var(--teal)"/>
    </svg>

    <div class="front-brand">
      <span class="brand-mark"></span>
      <span class="brand-name">Beacon Guard<br>Services</span>
    </div>

    <div class="person">
      <p class="person-name">Daniel Hofstra</p>
      <p class="person-role">Operations Manager</p>
    </div>

    <div class="address">
      <p class="line">
        <svg viewBox="0 0 12 12"><path d="M6 1 L11 6 H9.5 V11 H7 V8 H5 V11 H2.5 V6 H1 Z" fill="#fff"/></svg>
        1450 Harbor Line Rd.
      </p>
      <p class="indent">Marlow, TX 78110</p>
    </div>

    <div class="contacts">
      <p class="line">
        <svg viewBox="0 0 12 12"><path d="M3 1 L5 3.5 L4 5 Q5 7 7 8 L8.5 7 L11 9 L10 11 Q4 11 1 2 Z" fill="#fff"/></svg>
        0412 739 215
      </p>
      <p class="line">
        <svg viewBox="0 0 12 12"><rect x="1" y="5" width="10" height="6" rx="1" fill="#fff"/><rect x="3" y="1" width="6" height="4" fill="#fff"/></svg>
        0412 739 216
      </p>
      <p class="line">
        <svg viewBox="0 0 12 12"><rect x="1" y="2.5" width="10" height="7" rx="1" fill="#fff"/><path d="M1.5 3 L6 7 L10.5 3" stroke="var(--teal)" stroke-width="1" fill="none"/></svg>
        info@beaconguard.com.au
      </p>
      <p class="line">
        <svg viewBox="0 0 12 12"><circle cx="6" cy="6" r="5" fill="#fff"/></svg>
        www.beaconguard.com.au
      </p>
    </div>
  </section>

</main>
</body>
</html>
```